Business card design and logo needed - Photographer

I take photos of weddings, rodeos, snowmobiling.
Need a card to hand out to prospective clients.
Industry/Entity Type
Business
Contact Information for Business Card
Marcus Dolven Photography
Requirements
Must have
- Bold
Black or white base.
My website. www.MarcusDolven.example
Should not have
- camera/ lens/ aperture blades

```html
<!DOCTYPE html>
<html lang="en">
<head>
<meta charset="utf-8">
<title>Marcus Dolven Photography – Business Card</title>
<link rel="stylesheet" href="https://fonts.googleapis.com/css2?family=Open+Sans:wght@300;400&display=swap">
<style>
  :root {
    --page-bg: #e9e7e4;
    --card-bg: #2b2829;
    --text-main: #f4f3f1;
    --text-soft: #d9d7d4;
    --mark-grey: #b9b7b5;
    --divider: #151314;
  }
  html, body {
    margin: 0;
    width: 1200px;
    height: 900px;
    overflow: hidden;
    background: var(--page-bg);
    font-family: "Open Sans", Arial, sans-serif;
  }
  .card {
    position: absolute;
    left: 100px;
    top: 165px;
    width: 1000px;
    height: 571px;
    background: var(--card-bg);
    box-shadow: 0 12px 30px rgba(0,0,0,.25);
    overflow: hidden;
  }
  .brand {
    position: absolute;
    left: 125px;
    top: 236px;
    display: flex;
    align-items: center;
    gap: 22px;
    color: var(--text-main);
  }
  .brand-square {
    width: 78px;
    height: 78px;
    background: var(--mark-grey);
  }
  .brand-name {
    font-weight: 400;
    font-size: 44px;
    line-height: 1;
    letter-spacing: .5px;
  }
  .brand-sub {
    font-weight: 400;
    font-size: 17px;
    letter-spacing: 9px;
    margin-top: 10px;
    text-transform: uppercase;
  }
  .social-square {
    position: absolute;
    left: 540px;
    top: 392px;
    width: 20px;
    height: 20px;
    background: var(--text-soft);
  }
  .contact {
    position: absolute;
    right: 440px;
    top: 430px;
    text-align: right;
    color: var(--text-soft);
    font-weight: 300;
    font-size: 24px;
    line-height: 1.45;
    letter-spacing: .5px;
  }
  .gallery {
    position: absolute;
    left: 590px;
    top: 0;
    width: 410px;
    height: 100%;
    display: flex;
    gap: 4px;
    background: var(--divider);
  }
  .photo { height: 100%; }
  .photo-bride {
    flex: 0 0 158px;
    background: linear-gradient(160deg, #1c1918 0%, #4a3b33 45%, #8a7c74 75%, #2a2624 100%);
  }
  .photo-snow {
    flex: 0 0 118px;
    background: linear-gradient(180deg, #cfd3d6 0%, #e8e9e8 30%, #c9a21a 55%, #dfe1e2 80%, #b5b9bb 100%);
  }
  .photo-rodeo {
    flex: 1;
    background: linear-gradient(180deg, #5a5856 0%, #8b8a87 40%, #4d4b49 70%, #a7a5a1 100%);
  }
</style>
</head>
<body>
  <div class="card">
    <div class="brand">
      <div class="brand-square"></div>
      <div>
        <div class="brand-name">Marcus Dolven</div>
        <div class="brand-sub">Photography</div>
      </div>
    </div>

    <div class="social-square"></div>

    <div class="contact">
      <div>www.MarcusDolven.example</div>
      <div>(306) 555 0142</div>
    </div>

    <div class="gallery">
      <div class="photo photo-bride" role="img" aria-label="Wedding portrait of a bride in a strapless gown"></div>
      <div class="photo photo-snow" role="img" aria-label="Snowmobile rider in yellow gear among snowy trees"></div>
      <div class="photo photo-rodeo" role="img" aria-label="Black and white rodeo rider on horseback"></div>
    </div>
  </div>
</body>
</html>
```